Vellmora- plumbing service flyer

Hello,
We would like to create flyer for our plumbing company Vellmora
- we have 2 web domains
vellmora-example.hr ( official)
preuredbastanova-example.hr ( for bathroom renovation)

- we would like to create a similar Z-fold flyer ( from A4 paper) for our services
- We are sending images used on our websites. Of Course, it is allowed to put some of their own. Depending on design
- sending word with text which should go on each page. Text can be modified but in the sense of a page. The massage on a page should be as in word.
What is important to us:
- to stay in blue color
- It should be 1 page when fully open. So it looks like the complete page of information
- first/front page should be with our logo and phone number. more focus on emergency plumbing.
- back page should be about bathroom remodeling. Not necessary but would be received more points
- please don't use images of regular plumbers from Pixelgrove and similar. we don't want to use this stock's regular images as all others.

Target Market(s)

Bathroom remodeling and emergency plumbing

Industry/Entity Type

Construction-Plumbing

Colors
0054AA
0677BA
7BADD7
CADEEF
E8F1F8

Requirements
Must have
• Logo

```html
<!DOCTYPE html>
<html lang="en">
<head>
<meta charset="utf-8">
<title>Vellmora – Plumbing Service Flyer</title>
<link href="https://fonts.googleapis.com/css2?family=Saira+Condensed:wght@800&family=Montserrat:ital,wght@0,400;0,500;0,600;0,700;1,500;1,700&display=swap" rel="stylesheet">
<style>
  :root{
    --navy:#0d2f73;
    --blue:#0054aa;
    --blue-mid:#0677ba;
    --blue-soft:#7badd7;
    --blue-pale:#cadeef;
    --blue-mist:#e8f1f8;
    --red:#e41e26;
    --yellow:#f4b400;
    --ink:#1d2a44;
    --page:#383f47;
    --white:#ffffff;
  }
  *{box-sizing:border-box;margin:0;padding:0}
  html,body{width:1200px;height:3678px;overflow:hidden}
  body{background:var(--page);font-family:"Montserrat",sans-serif;color:var(--ink);position:relative}
  .spread{position:absolute;left:40px;width:1120px;height:868px;display:grid;grid-template-columns:repeat(3,1fr);background:var(--white);overflow:hidden}
  .spread--outer{top:941px}
  .spread--inner{top:1869px}
  .panel{position:relative;overflow:hidden}
  .panel > svg.bg{position:absolute;inset:0;width:100%;height:100%}
  .abs{position:absolute}
  .headline{font-family:"Saira Condensed",sans-serif;font-weight:800;line-height:.92;text-transform:uppercase;letter-spacing:.5px}
  .headline .blue{color:var(--blue)} .headline .red{color:var(--red)}
  .art{position:absolute}
  /* brand */
  .brand{display:flex;align-items:center;gap:8px;justify-content:center}
  .brand__dot{width:34px;height:34px;border-radius:50%;background:var(--white);border:4px solid var(--blue-mid)}
  .brand__name{font-family:"Saira Condensed",sans-serif;font-weight:800;font-size:30px;color:var(--white);letter-spacing:1px}
  /* outer left */
  .intro{left:38px;top:420px;width:310px;font-size:12.5px;line-height:1.25}
  .intro h2{font-family:"Saira Condensed",sans-serif;font-weight:800;font-size:40px;color:var(--red);margin-bottom:6px;line-height:1}
  .intro p{margin-bottom:9px}
  .intro .q{font-weight:600}
  .offer{list-style:none;margin-top:6px}
  .offer li{display:flex;align-items:center;gap:10px;font-size:11px;font-weight:700;color:var(--blue);margin-bottom:13px;line-height:1.1}
  .offer svg{width:24px;height:24px;flex:none}
  .tagline{color:var(--red);font-style:italic;font-weight:700;font-size:12px;line-height:1.1;margin-top:10px}
  /* emergency */
  .emergency{left:0;right:0;top:42px;text-align:center}
  .emergency .headline{font-size:40px}
  .emergency h3{font-weight:500;font-size:24px;color:var(--blue);margin:8px 0 10px}
  .svc{list-style:none;margin:0 38px}
  .svc li{font-size:11.5px;font-style:italic;font-weight:700;color:var(--blue);padding:5px 0 6px;border-top:1.5px dashed #9aa6b8}
  .svc li:last-child{border-bottom:1.5px dashed #9aa6b8}
  .emergency .note{font-size:11px;margin-top:10px;line-height:1.25}
  .emergency .daily{color:var(--red);font-weight:700;font-size:14px;margin-top:10px}
  .contact{left:0;right:0;top:640px;text-align:center;color:var(--white)}
  .contact .rule{display:flex;align-items:center;gap:10px;margin:14px 24px 6px}
  .contact .rule span{flex:1;height:2px;background:var(--white)}
  .contact .rule b{font-family:"Saira Condensed",sans-serif;font-weight:800;font-size:30px}
  .contact p{font-size:14px;line-height:1.65}
  /* services */
  .services{left:0;right:0;top:165px;text-align:center}
  .services .headline{font-size:44px;color:var(--blue)}
  .services ul{list-style:none;margin-top:8px}
  .services li{font-size:14px;font-weight:600;color:var(--navy);line-height:1.6;text-transform:uppercase}
  .services li::before{content:"";display:inline-block;width:8px;height:8px;border:1.5px solid var(--red);border-radius:50%;margin-right:5px;vertical-align:1px}
  .info{left:0;right:0;bottom:38px;text-align:center;font-size:14px;line-height:1.65;color:var(--ink)}
  .info .hl{color:var(--red)}
  /* steps */
  .steps{list-style:none;position:absolute}
  .step{position:relative;height:58px}
  .step .num{position:absolute;width:30px;height:30px;border-radius:50%;border:6px solid currentColor;background:var(--white);display:flex;align-items:center;justify-content:center}
  .step .num b{width:18px;height:18px;border-radius:50%;background:var(--navy);color:var(--white);font-size:8px;font-weight:700;display:flex;align-items:center;justify-content:center}
  .step .stem{position:absolute;top:13px;height:3px;background:currentColor}
  .step .label{position:absolute;font-size:13px;line-height:1.05;color:var(--ink);top:-6px;white-space:nowrap}
  .step .label--2{top:-20px}
  .step .label--3{top:-34px}
  .c-blue{color:var(--blue)} .c-red{color:var(--red)} .c-sky{color:#31a7e0} .c-yel{color:var(--yellow)} .c-pale{color:var(--blue-pale)}
  .check-title{left:30px;top:40px;width:320px;color:var(--white);font-style:italic;font-weight:700;font-size:23px;line-height:1.05}
  .checks{list-style:none;left:30px;top:170px;width:310px;color:var(--white)}
  .checks li{display:flex;gap:8px;font-size:14px;line-height:1.15;margin-bottom:22px}
  .checks svg{width:17px;height:17px;flex:none;margin-top:1px}
  .closing{left:24px;right:24px;top:618px;text-align:center;color:var(--red);font-style:italic;font-weight:700;font-size:12px;line-height:1.15}
  .callus{left:0;right:0;bottom:40px;text-align:center;color:var(--white);font-weight:700}
  .callus small{display:block;font-size:15px}
  .callus strong{font-size:24px;letter-spacing:.5px}
</style>
</head>
<body>

<!-- Outer side: front cover, emergency, services -->
<section class="spread spread--outer">

  <article class="panel panel--intro">
    <svg class="bg" viewBox="0 0 373 868" preserveAspectRatio="none" aria-hidden="true">
      <defs><linearGradient id="g1" x1="0" y1="0" x2="1" y2="1"><stop offset="0" stop-color="#0677ba"/><stop offset="1" stop-color="#0d2f73"/></linearGradient></defs>
      <rect width="373" height="868" fill="#f4f6f9"/>
      <polygon points="0,0 373,0 373,240 0,300" fill="url(#g1)"/>
      <polygon points="0,240 373,190 373,300 0,330" fill="#e41e26"/>
      <polygon points="0,285 373,228 373,285 0,345" fill="#f4f6f9"/>
    </svg>
    <div class="art" role="img" aria-label="Cartoon plumber superhero mascot flying with a thumbs up" style="left:40px;top:20px;width:290px;height:240px;border-radius:50%;background:radial-gradient(circle,#7badd7,#0677ba 70%,transparent 72%)"></div>
    <div class="intro abs">
      <h2>VELLMORA</h2>
      <p class="q">Do you need a<br>plumber for bathroom renovation?</p>
      <p class="q">Did your pipe burst or have some clogging in pipes ?</p>
      <p class="q">The neighbor's has ceiling leak?</p>
      <p>We offer plumbing services in the area of the City of Zagreb and its surroundings.</p>
      <p>Some of the common plumbing services include:</p>
      <ul class="offer">
        <li><svg viewBox="0 0 24 24" fill="none" stroke="#0054aa" stroke-width="2"><circle cx="12" cy="10" r="6"/><path d="M12 16v6M8 22h8"/></svg>Installation of new plumbing systems</li>
        <li><svg viewBox="0 0 24 24" fill="none" stroke="#0054aa" stroke-width="2"><path d="M4 4v16M20 4v16M4 12h16"/></svg>Repair of leaking pipes, faucets, &amp; fixtures</li>
        <li><svg viewBox="0 0 24 24" fill="none" stroke="#0054aa" stroke-width="2"><rect x="3" y="7" width="18" height="10"/><path d="M7 12h10"/></svg>Drain cleaning and unclogging</li>
        <li><svg viewBox="0 0 24 24" fill="none" stroke="#0054aa" stroke-width="2"><circle cx="12" cy="12" r="8"/><path d="M12 4v16"/></svg>Sewer line repair &amp; replacement</li>
        <li><svg viewBox="0 0 24 24" fill="none" stroke="#0054aa" stroke-width="2"><path d="M5 3v18M5 8h8v5H5M19 10v11"/></svg>Bathroom and kitchen plumbing installation and repair</li>
      </ul>
      <p class="tagline">Reliability, speed, accessibility.<br>Your Vellmora.</p>
    </div>
  </article>

  <article class="panel panel--emergency">
    <svg class="bg" viewBox="0 0 373 868" preserveAspectRatio="none" aria-hidden="true">
      <defs><linearGradient id="g2" x1="0" y1="0" x2="0" y2="1"><stop offset="0" stop-color="#0677ba"/><stop offset="1" stop-color="#0d2f73"/></linearGradient></defs>
      <rect width="373" height="868" fill="#fff"/>
      <polygon points="0,560 373,480 373,868 0,868" fill="url(#g2)"/>
    </svg>
    <div class="emergency abs">
      <div class="headline"><span class="blue">Emergency</span><br><span class="red">Plumbing</span></div>
      <h3>Emergency services:</h3>
      <ul class="svc">
        <li>Mechanical drain cleaning</li>
        <li>Water jet pipe cleaning</li>
        <li>Leak detections</li>
        <li>Pipe inspection with camera</li>
        <li>Thermal imaging of leakes</li>
        <li>Main pipe check up</li>
        <li>Valve change</li>
        <li>Change of sink siphon</li>
      </ul>
      <p class="note">Vellmora team will help<br>you to manage all the plumbing crises .</p>
      <p class="note">Fast and reliable</p>
      <p class="daily">CONTACT US DAILY 24/7</p>
    </div>
    <div class="contact abs">
      <div class="brand"><span class="brand__dot"></span><span class="brand__name">VELLMORA</span></div>
      <div class="rule"><span></span><b>CONTACT US</b><span></span></div>
      <p>info@vellmora-example.hr<br>+385 91 000 4821<br>www.vellmora-example.com<br>www.preuredbastanova-example.hr</p>
    </div>
  </article>

  <article class="panel panel--services">
    <svg class="bg" viewBox="0 0 373 868" preserveAspectRatio="none" aria-hidden="true">
      <defs><linearGradient id="g3" x1="0" y1="0" x2="1" y2="1"><stop offset="0" stop-color="#0677ba"/><stop offset="1" stop-color="#0054aa"/></linearGradient></defs>
      <rect width="373" height="868" fill="#fff"/>
      <polygon points="0,0 373,0 373,150 0,100" fill="url(#g3)"/>
      <polygon points="0,370 373,330 373,620 0,660" fill="#0d2f73"/>
      <polygon points="280,330 373,330 373,480" fill="#e41e26"/>
      <polygon points="0,560 90,660 0,660" fill="#e41e26"/>
    </svg>
    <div class="brand abs" style="left:0;right:0;top:50px"><span class="brand__dot"></span><span class="brand__name">VELLMORA</span></div>
    <div class="services abs">
      <div class="headline">Services :</div>
      <ul>
        <li>Bathroom remodeling</li>
        <li>Emergency plumbing</li>
        <li>Plumbing</li>
        <li>Lek detection</li>
      </ul>
    </div>
    <div class="art" role="img" aria-label="Cartoon plumber superhero mascot holding a pipe with a thumbs up" style="left:60px;top:360px;width:260px;height:290px;border-radius:40% 40% 10% 10%;background:linear-gradient(#7badd7,#0677ba)"></div>
    <div class="info abs">info@vellmora-example.hr<br>+385 91 000 4821<br>www.vellmora-example.com<br>www.<span class="hl">preuredbastanova-example</span>.hr</div>
  </article>
</section>

<!-- Inner side: plumbing steps, checklist, bathroom renovation -->
<section class="spread spread--inner">

  <article class="panel panel--plumbing">
    <svg class="bg" viewBox="0 0 373 868" preserveAspectRatio="none" aria-hidden="true">
      <rect width="373" height="868" fill="#f4f6f9"/>
      <polygon points="0,240 373,180 373,230 0,310" fill="#e41e26"/>
      <polygon points="0,300 373,220 373,268 0,320" fill="#fff"/>
    </svg>
    <div class="art" role="img" aria-label="Photo of a plumber working on wall pipes, blue toned" style="left:0;top:0;width:373px;height:250px;clip-path:polygon(0 0,100% 0,100% 72%,0 100%);background:linear-gradient(135deg,#3d6fb0,#0d2f73)"></div>
    <div class="abs headline" style="left:0;right:0;top:300px;text-align:center;font-size:38px"><span class="blue">Plumbing</span><br><span class="red">Steps :</span></div>
    <ol class="steps" style="left:0;top:410px;width:373px">
      <li class="step c-blue"><span class="stem" style="left:145px;width:75px"></span><span class="num" style="left:130px"><b>01</b></span><span class="label" style="left:212px;top:-10px">Planning faze</span></li>
      <li class="step c-red"><span class="stem" style="left:75px;width:105px"></span><span class="num" style="left:168px"><b>02</b></span><span class="label" style="left:40px;top:-10px">Demolition</span></li>
      <li class="step c-sky"><span class="stem" style="left:145px;width:75px"></span><span class="num" style="left:130px"><b>03</b></span><span class="label" style="left:212px;top:-10px">Plumbing faze</span></li>
      <li class="step c-yel"><span class="stem" style="left:75px;width:105px"></span><span class="num" style="left:168px"><b>04</b></span><span class="label" style="left:40px;top:-10px">Electric work</span></li>
      <li class="step c-blue"><span class="stem" style="left:145px;width:75px"></span><span class="num" style="left:130px"><b>05</b></span><span class="label" style="left:212px;top:-10px">Ceramic work</span></li>
      <li class="step c-red"><span class="stem" style="left:75px;width:105px"></span><span class="num" style="left:168px"><b>06</b></span><span class="label label--3" style="left:40px">Final<br>sanitary<br>installation</span></li>
      <li class="step c-pale"><span class="stem" style="left:145px;width:75px;background:var(--blue)"></span><span class="num" style="left:130px"><b>07</b></span><span class="label" style="left:212px;top:-10px">Plumbing faze</span></li>
    </ol>
  </article>

  <article class="panel panel--check">
    <svg class="bg" viewBox="0 0 373 868" preserveAspectRatio="none" aria-hidden="true">
      <defs><linearGradient id="g4" x1="0" y1="0" x2="0" y2="1"><stop offset="0" stop-color="#1a8fd6"/><stop offset=".6" stop-color="#0054aa"/><stop offset="1" stop-color="#0d2f73"/></linearGradient></defs>
      <rect width="373" height="868" fill="url(#g4)"/>
    </svg>
    <p class="check-title abs">What to check before installation and putting tiles on walls</p>
    <ul class="checks abs">
      <li><svg viewBox="0 0 20 20" fill="none" stroke="#fff" stroke-width="1.6"><circle cx="10" cy="10" r="8.5"/><path d="M6 10l3 3 5-6"/></svg>Decide on type of pipes:<br>PEX, PPR, Inox</li>
      <li><svg viewBox="0 0 20 20" fill="none" stroke="#fff" stroke-width="1.6"><circle cx="10" cy="10" r="8.5"/><path d="M6 10l3 3 5-6"/></svg>Inspect pipes with camera to check is pipe fall ok</li>
      <li><svg viewBox="0 0 20 20" fill="none" stroke="#fff" stroke-width="1.6"><circle cx="10" cy="10" r="8.5"/><path d="M6 10l3 3 5-6"/></svg>Test water pipes with test pump</li>
      <li><svg viewBox="0 0 20 20" fill="none" stroke="#fff" stroke-width="1.6"><circle cx="10" cy="10" r="8.5"/><path d="M6 10l3 3 5-6"/></svg>Take images of each wall with install pipes on it before closing. This steps will help you to be sure that installations are ok before closing.</li>
    </ul>
    <div class="art" role="img" aria-label="Cartoon plumber superhero mascot holding a pipe" style="left:10px;top:590px;width:230px;height:278px;border-radius:45% 45% 0 0;background:linear-gradient(#7badd7,#0677ba)"></div>
    <div class="art" role="img" aria-label="Illustration of connected pipes and yellow valves" style="left:240px;top:550px;width:133px;height:230px;border-radius:20px 0 0 60px;background:linear-gradient(90deg,#8a97a8,#5c6878)"></div>
  </article>

  <article class="panel panel--renovate">
    <svg class="bg" viewBox="0 0 373 868" preserveAspectRatio="none" aria-hidden="true">
      <rect width="373" height="868" fill="#fff"/>
      <polygon points="0,750 373,690 373,868 0,868" fill="#e41e26"/>
    </svg>
    <div class="abs headline" style="left:0;right:0;top:40px;text-align:center;font-size:38px"><span class="blue">Steps for</span><br><span class="red">renovating a</span><br><span class="red">bathroom:</span></div>
    <ol class="steps" style="left:0;top:205px;width:373px">
      <li class="step c-blue"><span class="stem" style="left:130px;width:62px"></span><span class="num" style="left:118px"><b>01</b></span><span class="label label--2" style="left:190px">Plan<br>your budget</span></li>
      <li class="step c-red"><span class="stem" style="left:60px;width:110px"></span><span class="num" style="left:160px"><b>02</b></span><span class="label label--2" style="left:22px">Plan<br>your design</span></li>
      <li class="step c-sky"><span class="stem" style="left:130px;width:62px"></span><span class="num" style="left:118px"><b>03</b></span><span class="label label--2" style="left:190px">Hire a<br>profesionals</span></li>
      <li class="step c-yel"><span class="stem" style="left:60px;width:110px"></span><span class="num" style="left:160px"><b>04</b></span><span class="label label--2" style="left:22px">Decide about<br>sanitary ware</span></li>
      <li class="step c-blue"><span class="stem" style="left:130px;width:62px"></span><span class="num" style="left:118px"><b>05</b></span><span class="label label--2" style="left:190px">Choose tile<br>and paint</span></li>
      <li class="step c-red"><span class="stem" style="left:60px;width:110px"></span><span class="num" style="left:160px"><b>06</b></span><span class="label label--3" style="left:22px">Install<br>bathroom<br>accessories</span></li>
      <li class="step c-blue"><span class="stem" style="left:130px;width:62px"></span><span class="num" style="left:118px"><b>07</b></span><span class="label" style="left:190px;top:-10px">Clean up</span></li>
    </ol>
    <p class="closing abs">By following these steps, you can successfully renovate your bathroom and create a space that meets your needs and style preferences.</p>
    <div class="callus abs"><small>CALL US:</small><strong>+385 91 000 4821</strong></div>
  </article>
</section>

</body>
</html>
```